依頼詳細
PCとスマホデザインの両方納品をいただきますが、
まずはデザインイメージが確認しやすいPCページのみの提案をお願いします。
スマホページは当選者に納品時にお願いしたいと思います。
スマホサイズは横幅750pxのサイズで作成してください。
(Lumexaディスプレイに対応するため)
レスポンシブウェブデザインを意識したデザインでお願いします。

■サイトマップ
添付の画面遷移図をご確認ください。

■参考サイト
https://kelparoute.com/
https://mivolune.jp/sportsevent/

■内容について
建築工務店が開催するイベント情報を掲載・告知をするサイトになります。
開催するイベント内容は添付のチラシのような内容の予定です。

■素材写真
画像データについては、フリー素材から流用して
イメージ画像に当て込んでください。
足りない場合は、一旦他のサイトの写真をサンプルとして
入れてください。(サンプルなどの表記をお願いします)
また、購入が必要な写真などを利用した場合、
価格とサイト名を教えてください。

また、Velmora Stockで定期契約をしていますので、
Velmora Stockの画像は使用できます。
デザイン時はカンプ画像をお入れいただきますようお願いします。

■ワイヤーフレーム
https://wire.pelvrin.com/view/a7392cdd-1148-4f0b-9d3e-e84521b07f3a-d318/
コンテンツの構成としてワイヤーフレームを作成しましたが
必ずしもワイヤーフレームの通りではなくて大丈夫です。
TOPページに配置するコンテンツを見ていただき、デザインは
デザイナーの皆様におまかせしたいと思います。

----------------------------------------------------------------------------
【制作物に対するお願い】

■サイズについて
TOPデザイン自体のアートボードサイズは、
横幅1366px、コンテンツ幅は1000pxでお願いします。
(縦幅の制限はございません)

■フォントについて
・無料で使えるフォントで作成をお願いします。
・OSに紐づくフォントの使用は控えていただければと思います (ヒラギノなど)

サイトURL
ページ数
1ページ
希望イメージ
シンプル 複雑
単色 カラフル
暗い 明るい
日常 高級
遊び心 厳粛
未来的 伝統的
女性的 男性的
希望する色
ベースカラー:白、緑 ポイントカラー:オレンジ
納品ファイル
• イラストレーター形式 (.ai)
• フォトショップ形式 (.psd)
補足説明
上記のいずれか1つ(アウトラインありとなしの2つ)と高解像度JPGを納品お願いします。
ロゴデータを追加で添付しました。

```html
<!DOCTYPE html>
<html lang="ja">
<head>
<meta charset="utf-8">
<title>イベント情報 | 青凪工務店</title>
<link href="https://fonts.googleapis.com/css2?family=M+PLUS+Rounded+1c:wght@500;700;800&family=Noto+Sans+JP:wght@400;500;700&display=swap" rel="stylesheet">
<style>
:root{
  --green:#2cb34a;
  --green-soft:#e6f4e6;
  --orange:#ee7a2f;
  --ink:#333;
  --muted:#777;
  --gray-bg:#f3f3f1;
  --white:#fff;
}
*{box-sizing:border-box;margin:0;padding:0}
html,body{width:1200px;height:3336px;overflow:hidden;background:var(--white)}
body{font-family:"Noto Sans JP",sans-serif;color:var(--ink);position:relative}
a{text-decoration:none}

.site-header{position:absolute;top:0;left:0;width:1200px;height:100px;z-index:3}
.brand{position:absolute;left:22px;top:18px;display:flex;align-items:center;gap:10px;font-family:"M PLUS Rounded 1c",sans-serif;font-weight:800;font-size:22px;color:var(--ink)}
.brand-mark{width:34px;height:34px;background:var(--ink)}
.social{position:absolute;right:180px;top:40px;display:flex;gap:14px}
.social span{width:18px;height:18px;border-radius:50%;background:var(--ink)}
.btn-apply{position:absolute;right:22px;top:28px;width:150px;height:44px;border-radius:22px;background:var(--orange);color:#fff;font-size:15px;font-weight:700;display:flex;align-items:center;justify-content:center}

.hero{position:absolute;top:0;left:0;width:1200px;height:620px;background:var(--green-soft)}
.hero svg.wave{position:absolute;bottom:0;left:0}
.hero-title{position:absolute;left:160px;top:200px;z-index:2}
.hero-title h1{font-family:"M PLUS Rounded 1c",sans-serif;font-weight:800;font-size:48px;color:var(--green);white-space:nowrap}
.hero-title p{font-size:16px;color:var(--green);letter-spacing:.12em;font-weight:700;margin-top:4px}
.hero-illust{position:absolute;left:480px;top:70px;width:660px;height:450px;border-radius:20px;background:linear-gradient(160deg,#f7fbf6,#dcecdc)}

.sec-head{position:absolute;left:0;width:1200px;text-align:center}
.sec-head h2{font-family:"M PLUS Rounded 1c",sans-serif;font-weight:800;font-size:32px}
.sec-head p{color:var(--orange);font-size:13px;font-weight:700;letter-spacing:.12em;margin-top:4px}
.deco{position:absolute;width:90px;height:70px;border-radius:10px;background:#eef2ee}

.cards{position:absolute;top:720px;left:180px;width:860px;display:grid;grid-template-columns:400px 400px;gap:60px}
.card{background:#fff;border-radius:10px;box-shadow:0 4px 18px rgba(0,0,0,.08);padding:20px;height:480px}
.card .photo{height:190px;border-radius:4px}
.card h3{font-family:"M PLUS Rounded 1c",sans-serif;color:var(--orange);font-size:19px;font-weight:800;line-height:1.5;margin:16px 0 12px;height:58px}
.meta dt{font-size:12px;color:var(--green);font-weight:700;margin-top:8px;display:flex;align-items:center;gap:6px}
.meta dt::before{content:"";width:9px;height:9px;border-radius:2px;background:var(--green)}
.meta dd{font-size:12px;color:var(--muted);margin-top:2px}

.btn-more{position:absolute;top:1818px;left:480px;width:240px;height:52px;border-radius:26px;background:var(--orange);color:#fff;font-weight:700;font-size:15px;display:flex;align-items:center;justify-content:center}

.news{position:absolute;top:1960px;left:0;width:1200px;height:480px;background:var(--gray-bg)}
.news-title{position:absolute;left:160px;top:110px;display:flex;align-items:baseline;gap:12px}
.news-title h2{font-family:"M PLUS Rounded 1c",sans-serif;font-weight:800;font-size:30px}
.news-title span{color:var(--orange);font-size:12px;font-weight:700}
.news-all{position:absolute;right:160px;top:122px;font-size:13px;color:var(--orange)}
.news-list{position:absolute;left:160px;top:180px;width:880px;list-style:none}
.news-list li{background:#fff;border-radius:30px;height:54px;margin-bottom:28px;display:flex;align-items:center;padding:0 26px;gap:28px;font-size:14px}
.news-list time{color:var(--orange);font-weight:700;font-size:13px}

.apply{position:absolute;top:2410px;left:0;width:1200px;height:400px;background:var(--green);color:#fff;text-align:center}
.apply h2{font-family:"M PLUS Rounded 1c",sans-serif;font-size:32px;font-weight:800;margin-top:70px}
.apply .en{font-size:13px;letter-spacing:.12em;font-weight:700;margin-top:4px}
.apply .lead{font-size:14px;margin-top:34px}
.apply .btn{display:inline-flex;width:260px;height:54px;border-radius:27px;background:#fff;color:var(--green);font-weight:700;font-size:15px;align-items:center;justify-content:center;margin-top:28px}
.apply-illust{position:absolute;top:90px;width:260px;height:290px;border-radius:16px;background:rgba(255,255,255,.16)}

.map{position:absolute;top:2810px;left:0;width:1200px;height:370px;background:linear-gradient(135deg,#eceee9,#dfe4dc)}
.pin{position:absolute;left:572px;top:110px;display:flex;align-items:center;gap:6px;font-size:14px;font-weight:700;color:#d33}

.site-footer{position:absolute;top:3180px;left:0;width:1200px;height:156px;background:#fff}
.site-footer .brand{top:34px;left:160px}
.foot-social{position:absolute;left:640px;top:44px;display:flex;gap:14px}
.foot-social span{width:18px;height:18px;border-radius:50%;background:var(--ink)}
.foot-links{position:absolute;right:160px;top:44px;display:flex;gap:30px;font-size:13px;color:var(--ink)}
.foot-links a{color:var(--ink)}
.copy{position:absolute;left:0;width:1200px;text-align:center;top:118px;font-size:11px;color:var(--muted)}
</style>
</head>
<body>

<section class="hero">
  <div class="hero-illust" role="img" aria-label="工具と作業員に囲まれた二階建ての家の線画イラスト"></div>
  <div class="hero-title">
    <h1>イベント情報</h1>
    <p>EVENT WEB SITE</p>
  </div>
  <svg class="wave" width="1200" height="80" viewBox="0 0 1200 80"><path d="M0 40 Q300 0 600 40 T1200 40 V80 H0Z" fill="#fff"/></svg>
</section>

<header class="site-header">
  <div class="brand"><span class="brand-mark"></span>青凪工務店</div>
  <div class="social"><span></span><span></span><span></span></div>
  <a class="btn-apply">お申し込み</a>
</header>

<div class="deco" style="top:600px;left:340px" role="img" aria-label="木製の椅子のイラスト"></div>
<div class="deco" style="top:600px;left:770px" role="img" aria-label="工具箱のイラスト"></div>
<div class="sec-head" style="top:610px"><h2>最新のイベント情報</h2><p>NEW EVENT</p></div>

<div class="cards">
  <article class="card">
    <div class="photo" role="img" aria-label="木の梁が見える新築セミナールームの写真" style="background:linear-gradient(135deg,#d8b98e,#a8825a)"></div>
    <h3>セミナープレイス LUMAREN 12月19日オープン イベント開催</h3>
    <dl class="meta"><dt>開催期間</dt><dd>2022年2月10日（木）〜2022年2月24日（木）</dd><dt>開催時間</dt><dd>10:00〜17:00</dd><dt>場所</dt><dd>青凪工務店敷地内　セミナープレイスLUMAREN</dd></dl>
  </article>
  <article class="card">
    <div class="photo" role="img" aria-label="机に並んだ手作りの木工道具箱の写真" style="background:linear-gradient(135deg,#c9b7a4,#8a6d55)"></div>
    <h3>冬休み木工教室を開催いたしました。ダミーです。</h3>
    <dl class="meta"><dt>開催期間</dt><dd>2022年2月10日（木）〜2022年2月24日（木）</dd><dt>開催時間</dt><dd>10:00〜17:00</dd><dt>場所</dt><dd>青凪工務店敷地内　セミナープレイスLUMAREN</dd></dl>
  </article>
  <article class="card">
    <div class="photo" role="img" aria-label="木製プランターに植えられた草花の写真" style="background:linear-gradient(135deg,#b59a74,#6f7d4d)"></div>
    <h3>西三条 工場の祭典。ダミーです。</h3>
    <dl class="meta"><dt>開催期間</dt><dd>2022年2月10日（木）〜2022年2月24日（木）</dd><dt>開催時間</dt><dd>10:00〜17:00</dd><dt>場所</dt><dd>青凪工務店敷地内　セミナープレイスLUMAREN</dd></dl>
  </article>
  <article class="card">
    <div class="photo" role="img" aria-label="緑のかごに盛られたぶどうの写真" style="background:linear-gradient(135deg,#8e4a5c,#3f8a4a)"></div>
    <h3>ぶどうの販売事。ダミーです。</h3>
    <dl class="meta"><dt>開催期間</dt><dd>2022年2月10日（木）〜2022年2月24日（木）</dd><dt>開催時間</dt><dd>10:00〜17:00</dd><dt>場所</dt><dd>青凪工務店敷地内　セミナープレイスLUMAREN</dd></dl>
  </article>
</div>

<a class="btn-more">イベント情報一覧</a>

<section class="news">
  <svg width="1200" height="60" viewBox="0 0 1200 60" style="position:absolute;top:-30px;left:0"><path d="M0 30 Q300 0 600 30 T1200 30 V60 H0Z" fill="#f3f3f1"/></svg>
  <div class="news-title"><h2>お知らせ</h2><span>NEWS</span></div>
  <span class="news-all">一覧を見る →</span>
  <ul class="news-list">
    <li><time>2022.02.01</time>セミナープレイス LUMAREN 12月19日オープン イベント開催。ダミーです。</li>
    <li><time>2022.02.01</time>冬休み木工教室を開催いたしました。ダミーです。</li>
    <li><time>2022.02.01</time>西三条 工場の祭典。ダミーです。</li>
  </ul>
</section>

<section class="apply">
  <div class="apply-illust" style="left:40px" role="img" aria-label="家と作業員の線画イラスト"></div>
  <div class="apply-illust" style="right:40px" role="img" aria-label="家族が並ぶ線画イラスト"></div>
  <h2>お申し込み</h2>
  <p class="en">APPLICATION</p>
  <p class="lead">各イベントへのお申し込みはこちらからお願いいたします。</p>
  <a class="btn">お申し込みフォーム</a>
</section>

<div class="map" role="img" aria-label="工務店周辺の地図">
  <div class="pin"><svg width="18" height="24" viewBox="0 0 18 24"><path d="M9 0C4 0 0 4 0 9c0 7 9 15 9 15s9-8 9-15c0-5-4-9-9-9z" fill="#d33"/><circle cx="9" cy="9" r="3.5" fill="#fff"/></svg>（株）青凪工務店</div>
</div>

<footer class="site-footer">
  <div class="brand"><span class="brand-mark"></span>青凪工務店</div>
  <div class="foot-social"><span></span><span></span><span></span></div>
  <nav class="foot-links"><a>プライバシーポリシー</a><a>サイトポリシー</a></nav>
  <p class="copy">Copyright © Aonagi Komuten Co., Ltd. All Rights Reserved.</p>
</footer>

</body>
</html>
```